Biz Cards for Lumivale Associates

Lumivale Associates is seeking a single-sided business card that is more visually-appealing than our current design (see attached).

Notes:
- Our colors are blue & teal.
- Our tag line must be large enough to be easily read
- We don't necessarily need our address included (that's just the biz office)
- We'd like to add our email address: Lumivale512@brindlemail.net

Thanks!

Industry/Entity Type

Business

Contact Information for Business Card

Standard size
PSD file required w/ text on its own layer

Colors
86cfc6
3277b5

```html
<!DOCTYPE html>
<html lang="en">
<head>
<meta charset="UTF-8">
<title>Lumivale Associates – Business Card</title>
<link href="https://fonts.googleapis.com/css2?family=Montserrat:wght@400;600;700&display=swap" rel="stylesheet">
<style>
  :root {
    --blue: #3277b5;
    --teal: #86cfc6;
    --teal-deep: #4fbfb2;
    --ink: #1d1d1f;
    --muted: #3a3a3c;
    --paper: #ffffff;
    --backdrop: #e6e7e9;
  }
  html, body {
    margin: 0;
    width: 1200px;
    height: 898px;
    overflow: hidden;
    background: var(--backdrop);
    font-family: "Montserrat", Arial, sans-serif;
  }
  .card {
    position: absolute;
    left: 120px;
    top: 175px;
    width: 960px;
    height: 548px;
    background: var(--paper);
    box-shadow: 0 10px 30px rgba(0,0,0,0.18);
    overflow: hidden;
  }
  .holder {
    position: absolute;
    left: 70px;
    top: 62px;
  }
  .holder-name {
    margin: 0;
    color: var(--blue);
    font-weight: 700;
    font-size: 34px;
    letter-spacing: 0.5px;
  }
  .holder-role {
    margin: 4px 0 0;
    color: var(--ink);
    font-weight: 400;
    font-size: 24px;
  }
  .contacts {
    position: absolute;
    left: 70px;
    bottom: 70px;
    margin: 0;
    padding: 0;
    list-style: none;
  }
  .contacts li {
    display: flex;
    align-items: center;
    gap: 22px;
    font-size: 23px;
    color: var(--muted);
    line-height: 36px;
  }
  .contacts svg {
    width: 22px;
    height: 22px;
    fill: var(--blue);
  }
  .brand {
    position: absolute;
    right: 60px;
    top: 220px;
    text-align: center;
    width: 440px;
  }
  .brand-mark {
    width: 54px;
    height: 54px;
    border-radius: 50%;
    background: var(--teal);
    margin: 0 auto 14px;
  }
  .brand-name {
    margin: 0;
    font-size: 46px;
    font-weight: 600;
    color: var(--ink);
    letter-spacing: 1px;
    line-height: 1.05;
  }
  .brand-suffix {
    margin: 4px 0 0;
    font-size: 22px;
    font-weight: 600;
    color: var(--ink);
    letter-spacing: 9px;
  }
  .tagline {
    position: absolute;
    right: 40px;
    top: 400px;
    margin: 0;
    font-size: 21px;
    font-weight: 700;
    color: var(--ink);
    white-space: nowrap;
  }
  .tagline .sep {
    color: var(--blue);
    font-weight: 400;
    margin: 0 6px;
  }
  .band {
    position: absolute;
    left: 0;
    bottom: 0;
    width: 960px;
    height: 30px;
  }
</style>
</head>
<body>
  <div class="card">
    <div class="holder">
      <h1 class="holder-name">Maren Calloway, RN</h1>
      <p class="holder-role">Mental Health Therapist</p>
    </div>

    <ul class="contacts">
      <li>
        <svg viewBox="0 0 24 24" aria-hidden="true"><path d="M7 1h10a2 2 0 0 1 2 2v18a2 2 0 0 1-2 2H7a2 2 0 0 1-2-2V3a2 2 0 0 1 2-2zm0 3v14h10V4H7zm5 15.5a1 1 0 1 0 0 2 1 1 0 0 0 0-2z"/></svg>
        (855) LUM-VALE
      </li>
      <li>
        <svg viewBox="0 0 24 24" aria-hidden="true"><path d="M6 2h12v5H6zM3 8h18a2 2 0 0 1 2 2v7h-4v5H5v-5H1v-7a2 2 0 0 1 2-2zm4 8v4h10v-4H7z"/></svg>
        (330) 555-0142
      </li>
      <li>
        <svg viewBox="0 0 24 24" aria-hidden="true"><path d="M2 5h20v2l-10 6L2 7zm0 4.3l10 6 10-6V19H2z"/></svg>
        Lumivale512@brindlemail.net
      </li>
      <li>
        <svg viewBox="0 0 24 24" aria-hidden="true"><path d="M10 2a8 8 0 0 1 6.3 12.9l5.4 5.4-2.1 2.1-5.4-5.4A8 8 0 1 1 10 2zm0 3a5 5 0 1 0 0 10 5 5 0 0 0 0-10z"/></svg>
        Lumivale.net
      </li>
    </ul>

    <div class="brand">
      <div class="brand-mark"></div>
      <p class="brand-name">LUMIVALE</p>
      <p class="brand-suffix">ASSOCIATES Ltd</p>
    </div>

    <p class="tagline">Clear Minds<span class="sep">|</span>Kind Hearts<span class="sep">|</span>Steady Care</p>

    <svg class="band" viewBox="0 0 960 30" preserveAspectRatio="none" aria-hidden="true">
      <rect x="0" y="0" width="960" height="30" fill="var(--teal-deep)"/>
      <polygon points="470,0 960,0 960,30 455,30" fill="var(--blue)"/>
    </svg>
  </div>
</body>
</html>
```